Property Portal needs Chatterbook Cover Image and Sponsor Ad Design

WHO WE ARE
Hi Pitchers! We are an advertising portal that focus on presenting the latest property launches in Singapore. Our platform and interface will provide consumer an enjoyable and easy browsing experience looking for their ideal property to buy/invest, while ensuring updated information, images/videos, and other useful description is provided on each project.

WHAT WE NEED
Our website is www.brightkeyhomes.sg, and we need designs for our Chatterbook page www.facebook.com/brightkeyhomes. One as the Cover Image (815 x 315), and one as our Sponsor Ad Image (1200 x 627). The 2 designs can be similar or different.

DESIGN
We want to convey a professional and sociable feel. A "cool" and elegant design may be suitable, although feel free to have your own look & feel as long as it suits our purpose. Try to have a focus, and not look messy. We don't want to look cheap, spammy or boring in any sense. Be creative and purposeful =) You may use the snapvault images attached or you can use your own. Add symbols or graphics if it helps to give the design a better feel.

For your reference, I find there is a number of good designs with nice look & feel in this project including those withdraw/eliminated.
http://social.pitchhive.com/contest.aspx?id=718206&page=2
http://social.pitchhive.com/contest.aspx?id=718206

IDEAS
You may want to embed our portal in an SLATEPAD device as part of the design (see samples below but replace slatephone with SlatePad). And/or you can have a blur-out image background to have a focus on what you want to show. Please note that we are not restricting any other designs concept, this is just an idea I have.

CAPTIONS
You may use one or a few of the sample captions below.
- Singapore Latest Property Launches In One Portal (slight emphasis on "in one portal")
- Latest Projects • Updated Info • Best Pricing
- Residential • Commercial • Overseas (perhaps label on images)

Hope we can find an ideal design here. We will request from pitchhive to increase the project budget to give out more participation payments if there is a few good ones. We are also looking to find suitable designers for our future projects as we need a few more designs. If you have questions, feel free to ask me and I will reply promptly.
Updates

Reason: Project cancelled and relaunch with different purpose, moved from Newsletter to Chatterbook Design.

IDEAS (UPDATED) I am thinking one way to showcase our portal is perhaps to have our website embedded in an slatepad and/or pebblebook device as part of the design. I've attached some designs I came across to show what I mean (only the embedding part). If you are going to do it this way, you can use our main page www.brightkeyhomes.sg and/or a project page www.brightkeyhomes.sg/lakeshade-at-morrowdale to display

Target Market(s)

Real Estate Agents, Investors, Developers, General public age 30 & above

Industry/Entity Type

Advertising

Colors
9ccb3b
00a98f
0592cd
3176b5
ffcf3e
5c5c5c

Requirements
Should not have
• I prefer not to use real people stock images unless you are very sure it will work out well.

```html
<!DOCTYPE html>
<html lang="en">
<head>
<meta charset="utf-8">
<title>Singapore Latest Property Launches In One Portal</title>
<link rel="stylesheet" href="https://fonts.googleapis.com/css2?family=Oswald:wght@300;400&family=Open+Sans:wght@400;600;700&display=swap">
<style>
:root{
  --green:#8cc63f;
  --green-dark:#1f8a45;
  --green-nav:#2e9d58;
  --night-1:#1a1a2e;
  --night-2:#3a2a4a;
  --warm:#b07a3a;
  --white:#ffffff;
  --ink:#333333;
  --muted:#777777;
  --paper:#f4f4f4;
  --footer:#9b9b9b;
  --footer-dark:#7c7c7c;
  --social:#3b5998;
}
*{margin:0;padding:0;box-sizing:border-box}
html,body{width:1200px;height:627px;overflow:hidden;background:#000}
.ad{position:relative;width:1200px;height:627px;overflow:hidden;font-family:"Open Sans",Arial,sans-serif}
.ad-backdrop{position:absolute;inset:0;
  background:
    radial-gradient(ellipse at 22% 38%,rgba(214,160,80,.75) 0%,rgba(140,90,50,.45) 30%,transparent 60%),
    radial-gradient(ellipse at 90% 20%,rgba(170,120,170,.6) 0%,transparent 55%),
    linear-gradient(180deg,#3c2f52 0%,#4a3a55 35%,#2a2a38 70%,#1b2a3a 100%);}
.headline-band{position:absolute;left:0;top:270px;width:522px;height:115px;background:rgba(20,20,20,.55)}
.headline{position:absolute;left:180px;top:288px;color:var(--white);font-family:"Oswald",sans-serif;font-weight:300;font-size:33px;line-height:46px;letter-spacing:.3px}
.headline .emphasis{display:inline-block;background:var(--green);padding:0 12px;margin-left:12px;line-height:40px;font-weight:400}

.site{position:absolute;left:783px;top:104px;width:305px;height:472px;background:var(--paper);box-shadow:0 4px 18px rgba(0,0,0,.55);font-size:3.4px;color:var(--ink)}
.site-logo{position:absolute;top:9px;left:0;width:100%;text-align:center;font-size:11px;font-weight:700;color:var(--green-dark)}
.site-logo .mark{display:inline-block;width:9px;height:9px;border-radius:50%;background:var(--green);margin-right:3px;vertical-align:-1px}
.site-links{position:absolute;top:31px;left:108px;display:flex;gap:6px;font-size:3.6px;color:var(--muted)}
.site-nav{position:absolute;left:28px;top:36px;width:247px;height:18px;background:linear-gradient(var(--green-nav),var(--green-dark));display:flex;align-items:center;justify-content:space-around;color:var(--white);font-size:3.3px}
.site-banner{position:absolute;left:28px;top:54px;width:247px;height:87px;background:linear-gradient(180deg,#e9eef0 0%,#cfdde0 45%,#6d9a6a 75%,#3f6f4a 100%)}
.banner-title{position:absolute;left:8px;top:6px;font-family:"Oswald",sans-serif;font-size:7px;letter-spacing:2px;color:#555}
.banner-tag{position:absolute;left:8px;top:20px;font-size:4px;font-style:italic;color:#444}
.site-grid{position:absolute;left:28px;top:164px;width:177px;height:221px;background:var(--white);display:grid;grid-template-columns:1fr 1fr;gap:3px;padding:3px}
.card{text-align:center;position:relative}
.card-photo{height:40px;margin:3px 4px 0;background:linear-gradient(180deg,#b9d3df,#5f8f73)}
.card-name{font-family:"Oswald",sans-serif;font-size:6px;margin:4px 0 2px}
.card ul{list-style:none;text-align:left;padding-left:8px;line-height:5.4px}
.card ul li::before{content:"■ ";color:#444}
.card-btn{position:absolute;bottom:2px;left:50%;transform:translateX(-50%);border:.5px solid #999;padding:1px 5px;font-weight:700;font-size:3px}
.site-side{position:absolute;left:207px;top:164px;width:68px;height:221px;background:var(--white);padding:5px}
.side-title{font-style:italic;font-size:5px;color:#555;border-bottom:.5px solid #ccc;margin-bottom:4px}
.side-label{margin-top:4px}
.side-field{height:4px;border:.5px solid #aaa;margin-top:1px}
.side-list{height:26px;border:.5px solid #aaa;margin-top:1px}
.side-btn{float:right;margin-top:2px;border:.5px solid #888;padding:0 3px}
.site-footer{position:absolute;left:0;top:386px;width:305px;height:86px;background:var(--footer);color:var(--white);display:flex;gap:14px;padding:8px 0 0 28px;font-size:3px;line-height:5px}
.footer-col b{font-weight:600}
.footer-social{position:absolute;left:193px;top:51px;width:34px;height:9px;background:var(--social)}
.footer-bar{position:absolute;left:28px;top:72px;width:247px;height:12px;background:var(--footer-dark);text-align:center;font-size:2.8px;padding-top:2px}
</style>
</head>
<body>
<main class="ad">
  <div class="ad-backdrop" role="img" aria-label="Night view of lit condominium towers beside a pool and palm trees"></div>
  <div class="headline-band"></div>
  <h1 class="headline">Singapore Latest Property<br>Launches<span class="emphasis">In One Portal</span></h1>

  <section class="site" aria-label="Portal home page">
    <div class="site-logo"><span class="mark"></span>brightkeyhomes.sg</div>
    <nav class="site-links"><span>Home</span><span>About Us</span><span>Contact Us</span><span>Useful Guides</span></nav>
    <nav class="site-nav"><span>Apartment / Condo</span><span>Executive Condo</span><span>Cluster House</span><span>Commercial</span><span>Industrial</span><span>Overseas</span></nav>
    <div class="site-banner" role="img" aria-label="Riverside condominium towers among green trees">
      <div class="banner-title">LAKESHADE</div>
      <div class="banner-tag">A Truly Riverfront Living at Morrowdale</div>
    </div>
    <div class="site-grid">
      <article class="card"><div class="card-photo" role="img" aria-label="Project render"></div><div class="card-name">Verdantis</div><ul><li>Executive Condo • 99 years</li><li>District 19 North East</li><li>510 units • 2BR to 5BR</li><li>TOP 2019</li></ul><span class="card-btn">VIEW THIS PROJECT</span></article>
      <article class="card"><div class="card-photo" role="img" aria-label="Project render"></div><div class="card-name">Harbourview @ Kent</div><ul><li>Condominium • 99 years</li><li>District 05 West</li><li>210 units • 2BR to 4BR</li><li>TOP 2018</li></ul><span class="card-btn">VIEW THIS PROJECT</span></article>
      <article class="card"><div class="card-photo" role="img" aria-label="Project render"></div><div class="card-name">Crestfield Towers</div><ul><li>Condominium • 99 years</li><li>District 03 Central</li><li>845 units • 1BR to 4BR</li><li>TOP 2020</li></ul><span class="card-btn">VIEW THIS PROJECT</span></article>
      <article class="card"><div class="card-photo" role="img" aria-label="Project render"></div><div class="card-name">The Solvara</div><ul><li>Condominium • 99 years</li><li>District 18 East</li><li>597 units • 1BR to 5BR</li><li>TOP 2019</li></ul><span class="card-btn">VIEW THIS PROJECT</span></article>
    </div>
    <aside class="site-side">
      <div class="side-title">Quick Search</div>
      <div class="side-label">Property Type</div><div class="side-field"></div>
      <div class="side-label">District / Region</div><div class="side-field"></div>
      <div class="side-label">Property That Is</div><div class="side-list"></div>
      <div class="side-label">Search by Name</div><div class="side-field"></div>
      <span class="side-btn">Search</span>
      <div class="side-title" style="margin-top:14px">Subscribe With Us</div>
      <div class="side-label">Email address</div><div class="side-field"></div>
      <div class="side-label">Contact number</div><div class="side-field"></div>
    </aside>
    <footer class="site-footer">
      <div class="footer-col"><b>Property Type</b><br>Apartment / Condo<br>Executive Condo<br>Cluster House<br>Commercial</div>
      <div class="footer-col"><b>By District</b><br>D01 - D08 Central<br>D09 - D11 Orchard<br>D12 - D15 East<br>D19 - D23 North</div>
      <div class="footer-col"><b>Property That Is</b><br>Freehold<br>New Launch<br>Completed<br>Waterfront</div>
      <div class="footer-col"><b>Overseas</b><br>Malaysia<br>Australia<br>UK</div>
      <div class="footer-social"></div>
      <div class="footer-bar">About Us • Contact Us • Advertise With Us • Terms Of Use<br>Copyright © brightkeyhomes.sg All Rights Reserved</div>
    </footer>
  </section>
</main>
</body>
</html>
```